Bold Website Design for Fitness Trainer - No Coding

We are in need of a bold and unique website design for a personal fitness training company, www.TessaLorvel.com. We need DESIGN ONLY for three pages. These will be a homepage, a lead capture page, and one internal page with a sidebar. The design will be used for coding a wordpress theme, if that matters for the designer.

Tessa Lorvel Fitness Training
2738 E 19th St #415
Austin, TX 78705
512-607-4918
http://www.tessalorvel.com

Target Market(s)

18-45 year old male and females making 80k+ a year and looking to get stronger and in shape.

Industry/Entity Type

Fitness

Number of Pages Required

3 page

Font styles to use
Sans Serif

Requirements
Must have
• See attached design specs file.
Nice to have
Should not have
• Boxed layout.
• Dark Background.

```html
<!DOCTYPE html>
<html lang="en">
<head>
<meta charset="utf-8">
<title>Tessa Lorvel Fitness Training</title>
<link rel="stylesheet" href="https://fonts.googleapis.com/css2?family=Montserrat:wght@400;600;700;800&family=Open+Sans:ital,wght@0,400;0,600;0,700;1,700&display=swap">
<style>
:root{
  --pink:#ec2a91;
  --cyan:#00b3ec;
  --ink:#1a1a1a;
  --topbar:#2b2b2b;
  --yellow:#ffe500;
  --white:#ffffff;
  --card:#f5f5f5;
  --grey:#444;
}
*{margin:0;padding:0;box-sizing:border-box}
html,body{width:1200px;height:968px;overflow:hidden;background:var(--white);font-family:"Open Sans",Arial,sans-serif;color:var(--ink)}
.page{position:relative;width:1200px;height:968px}
.topbar{position:absolute;top:0;left:0;width:1200px;height:20px;background:linear-gradient(#3a3a3a,#222)}
.topbar-links{position:absolute;left:382px;top:3px;display:flex;gap:18px;font:700 9px "Open Sans",sans-serif;color:var(--white)}
.topbar-links span{display:flex;align-items:center;gap:4px}
.social{position:absolute;left:752px;top:3px;display:flex;gap:4px}
.social i{display:block;width:13px;height:13px;border-radius:50%;background:#eee}
.brand{position:absolute;top:28px;left:0;width:1200px;display:flex;justify-content:center;align-items:center;gap:8px}
.brand-dot{width:52px;height:52px;border-radius:50%;background:var(--yellow)}
.brand-name{font:800 19px "Montserrat",sans-serif;color:var(--cyan);line-height:1.05;width:130px}
.nav{position:absolute;top:96px;left:0;width:1200px;height:21px;background:var(--pink)}
.nav ul{position:absolute;left:386px;display:flex;list-style:none;height:21px}
.nav li{font:600 8.5px "Open Sans",sans-serif;color:var(--white);padding:0 11px;line-height:21px}
.nav li.cta{background:var(--cyan);margin-left:6px;padding:0 11px}
.hero{position:absolute;top:117px;left:0;width:1200px;height:189px;background:#000}
.hero-photo{position:absolute;left:335px;top:0;width:530px;height:189px;background:radial-gradient(ellipse at 50% 45%,#8a8a8a 0%,#444 45%,#111 85%)}
.hero h1{position:absolute;top:113px;left:0;width:1200px;text-align:center;font:700 15px "Montserrat",sans-serif;color:var(--white)}
.signup{position:absolute;top:306px;left:0;width:1200px;height:129px;background:var(--cyan);text-align:center}
.signup h2{margin-top:19px;font:800 21px "Montserrat",sans-serif;color:var(--ink)}
.signup h3{margin-top:5px;font:700 14px "Montserrat",sans-serif;color:var(--white)}
.signup .tags{margin-top:2px;font:700 8px "Open Sans",sans-serif;color:#6fd8f7;letter-spacing:.3px}
.btn-dark{display:inline-block;margin-top:12px;background:#111;color:var(--yellow);font:700 11px "Montserrat",sans-serif;padding:4px 12px;border:1px solid #7de3ff}
.intro{position:absolute;top:467px;left:410px;width:380px;text-align:center;font-size:8.5px;line-height:12.5px;color:var(--grey)}
.btn-outline{position:absolute;top:528px;left:566px;width:68px;height:17px;border:1.5px solid #111;font:700 8px "Montserrat",sans-serif;text-align:center;line-height:14px}
.card{position:absolute;top:571px;width:140px;height:247px;background:var(--card);border-bottom:3px solid var(--pink);box-shadow:0 1px 3px rgba(0,0,0,.2)}
.card h4{height:29px;background:var(--pink);color:var(--white);font:700 8.5px "Montserrat",sans-serif;text-align:center;line-height:38px}
.card-photo{width:108px;height:108px;border-radius:50%;margin:23px auto 0;background:radial-gradient(circle,#cfcfcf,#6a6a6a)}
.card p{margin:14px 12px 0;text-align:center;font-size:6.5px;line-height:10px;color:var(--grey)}
.testimonials{position:absolute;top:806px;left:0;width:1200px;height:162px;background:#000}
.testimonials-bg{position:absolute;left:350px;top:0;width:500px;height:162px;background:radial-gradient(ellipse,#3a3a3a,#0a0a0a 80%)}
.testimonials h5{position:absolute;top:34px;left:0;width:1200px;text-align:center;font:700 13px "Montserrat",sans-serif;color:var(--pink)}
.client-photo{position:absolute;left:433px;top:58px;width:60px;height:60px;border-radius:50%;background:radial-gradient(circle,#8a7a6a,#3a3a3a);border:2px solid #ddd}
.client-name{position:absolute;left:420px;top:924px;width:86px;text-align:center;font:italic 400 7.5px "Open Sans",sans-serif;color:#ccc;margin-top:-806px}
.quote{position:absolute;left:509px;top:70px;width:300px;font:italic 700 7.5px "Open Sans",sans-serif;line-height:10px;color:var(--yellow)}
.arrow{position:absolute;top:78px}
</style>
</head>
<body>
<div class="page">
  <header class="topbar">
    <div class="topbar-links">
      <span><svg width="8" height="9" viewBox="0 0 8 9"><path d="M1 1h2l1 2-1 1a5 5 0 0 0 2 2l1-1 2 1v2H6A6 6 0 0 1 1 1z" fill="#ec2a91"/></svg>(512) 607-4918</span>
      <span><svg width="7" height="9" viewBox="0 0 7 9"><path d="M3.5 0A3.5 3.5 0 0 1 7 3.5C7 6 3.5 9 3.5 9S0 6 0 3.5A3.5 3.5 0 0 1 3.5 0z" fill="#ec2a91"/><circle cx="3.5" cy="3.5" r="1.3" fill="#2b2b2b"/></svg>LOCATION</span>
      <span><svg width="8" height="8" viewBox="0 0 8 8"><rect width="8" height="8" rx="1" fill="#ec2a91"/><rect x="1" y="3" width="6" height="4" fill="#2b2b2b"/></svg>CALENDAR</span>
    </div>
    <div class="social"><i></i><i></i><i></i><i></i></div>
  </header>

  <div class="brand">
    <div class="brand-dot"></div>
    <div class="brand-name">Tessa Lorvel Fitness Training</div>
  </div>

  <nav class="nav">
    <ul>
      <li>HOME</li><li>PROGRAMS</li><li>MEET YOUR TRAINER</li><li>BLOG</li><li>CONTACT ME</li><li class="cta">FREE SESSION!</li>
    </ul>
  </nav>

  <section class="hero">
    <div class="hero-photo" role="img" aria-label="Black and white photo of hands gripping a loaded barbell"></div>
    <h1>AUSTIN'S #1 PERSONAL TRAINER</h1>
  </section>

  <section class="signup">
    <h2>GET STARTED TODAY!</h2>
    <h3>Your First Session is FREE!</h3>
    <div class="tags">GENERAL FITNESS - WEIGHT LOSS - STRENGTH TRAINING - POWERLIFTING</div>
    <span class="btn-dark">SIGN UP NOW ››</span>
  </section>

  <p class="intro">CoreFlex is constantly varied, functional movements executed at high intensity.<br>Our program gives you a more balanced overall fitness, increasing your capability and capacity over a broader range of movements and activities. And what we do is scalable to accommodate different levels of experiences, injury or other limiting factors.</p>
  <div class="btn-outline">READ MORE</div>

  <article class="card" style="left:381px">
    <h4>1-ON-1 PERSONAL TRAINING</h4>
    <div class="card-photo" role="img" aria-label="Trainer assisting a client with a stretch band"></div>
    <p>Tessa specializes in personal training conducting Weight Loss and Nutrition programs in addition to strength training sessions &amp; Boot Camps</p>
  </article>
  <article class="card" style="left:531px">
    <h4>ONLINE COACHING</h4>
    <div class="card-photo" role="img" aria-label="Athlete lifting a kettlebell"></div>
    <p>We will capture your individual fitness goals and provide the tools and training necessary to achieve them.</p>
  </article>
  <article class="card" style="left:680px">
    <h4>STRENGTH PROGRAMMING</h4>
    <div class="card-photo" role="img" aria-label="Athlete holding a barbell in a gym"></div>
    <p>A proper program can provide significant functional benefits and improvement in overall health and well-being.</p>
  </article>

  <section class="testimonials">
    <div class="testimonials-bg" role="img" aria-label="Dark gym interior background"></div>
    <h5>Words from my Clients</h5>
    <svg class="arrow" style="left:386px" width="10" height="26" viewBox="0 0 10 26"><path d="M9 1 1 13l8 12" fill="none" stroke="#ccc" stroke-width="1"/></svg>
    <svg class="arrow" style="left:810px" width="10" height="26" viewBox="0 0 10 26"><path d="m1 1 8 12-8 12" fill="none" stroke="#ccc" stroke-width="1"/></svg>
    <div class="client-photo" role="img" aria-label="Client portrait"></div>
    <p class="quote">Tessa's training methods are addictive and will leave you wanting more after every workout. Everyday has new challenging workouts and its impossible to get bored with it. Whether you're a fitness pro for years or just starting out, it's a great environment and an even better community to join. Delighted to recommend!</p>
  </section>
  <div class="client-name" style="position:absolute;top:930px;left:420px;margin:0">Dario Quent</div>
</div>
</body>
</html>
```